PlayerMetricsHubOnline - Game Statistics and Achievement Tracking

I need a new modern design for an existing website.

The website is a project to track statistics and achievements for games (currently Vaporo Achievements/Stats and stats for Continental Hauler Pro 2 and Prairie Freight Commander).
I am currently expanding the site with other platforms (like QLV) and more games.
I am also adding a user registration/signin with user profiles to show off their achievements and stats across all platforms and games.

The current website is available at https://plymetrx.example/
To search for data you can use the username "pixeldorian" (without quotes).

The design should be modern and extendable and contain space for a logo.

The logo should match the project. It should combine Gaming with statistics.

Target Market(s)

Video game players

Number of Pages Required

5+ page

Font styles to use
Sans Serif

Requirements
Must have
• Basic Layout, User profile page (not yet available on live site), Search Page for Platforms/Games, Platform profile page, Dark theme

```html
<!DOCTYPE html>
<html lang="en">
<head>
<meta charset="utf-8">
<title>PlayerMetricsHubOnline – Search for Platforms/Games</title>
<link rel="stylesheet" href="https://fonts.googleapis.com/css2?family=Inter:wght@400;500;600;700&display=swap">
<style>
:root{
  --blue:#1765ff;
  --ink:#ffffff;
  --muted:#c9c9cf;
  --page:#1c1c1e;
  --panel:#0f0f10;
  --nav:#121213;
  --card:#141415;
  --footer:#1f1f21;
  --line:#3a3a3e;
  --stage:#ffffff;
}
*{box-sizing:border-box;margin:0;padding:0}
html,body{width:1200px;height:2799px;overflow:hidden;background:var(--stage)}
body{font-family:"Inter",Arial,sans-serif;color:var(--ink)}
.canvas{position:relative;width:1200px;height:2799px;overflow:hidden;background:var(--stage)}
.stage-band{position:absolute;inset:0;width:1200px;height:2799px}
.abs{position:absolute}

.brand{font-weight:600;color:var(--ink);white-space:nowrap}
.nav{position:absolute;left:0;top:0;width:100%;background:var(--nav);display:flex;align-items:center}
.nav-links{position:absolute;display:flex;gap:8px;font-size:7px;color:var(--ink);white-space:nowrap}
.signin{position:absolute;font-size:7px;text-decoration:underline;color:var(--ink)}
.btn{background:var(--blue);color:#fff;border-radius:3px;display:flex;align-items:center;justify-content:center;gap:4px;font-weight:500;white-space:nowrap}
.hero-photo{position:absolute;background:
  radial-gradient(circle at 72% 55%,#d11a73 0,#8a1457 25%,transparent 50%),
  radial-gradient(circle at 85% 15%,#f03a8f 0,transparent 30%),
  linear-gradient(115deg,#2c2a36 0%,#4a2040 35%,#6b1a52 55%,#2a1e4a 80%,#161a3a 100%)}
.hero-copy{position:absolute}
.hero-brand{font-weight:500;white-space:nowrap}
.hero-title{font-weight:500;line-height:1.1}
.search-panel{position:absolute;background:var(--panel);border-radius:3px}
.search-panel h3{position:absolute;font-weight:600}
.field{position:absolute;background:#fff;color:#6b6b70;display:flex;align-items:center;white-space:nowrap}
.adv{position:absolute;color:var(--blue);text-decoration:underline;white-space:nowrap}
.caret{width:0;height:0;border-left:3px solid transparent;border-right:3px solid transparent;border-top:3px solid #555}

.card{position:absolute;width:121px;height:123px;background:var(--card);display:flex;flex-direction:column}
.cover{height:58px;width:100%}
.card-body{padding:5px 8px 0;display:flex;flex-direction:column;flex:1}
.card-title{font-size:7.5px;font-weight:600;margin-top:2px;white-space:nowrap}
.card-text{font-size:5.8px;line-height:1.3;margin-top:7px;color:#e6e6ea}
.card-meta{display:flex;align-items:center;gap:5px;font-size:5.8px;margin-top:auto;margin-bottom:9px}
.os{display:flex;gap:2px}
.os i{display:block;width:5px;height:5px;background:#fff}
.sep{width:1px;height:6px;background:#fff}
.play{margin-left:auto;background:var(--blue);border-radius:5px;font-size:4.5px;padding:1px 5px}
.card--lg{width:195px;height:154px}
.card--lg .cover{height:76px}
.card--lg .card-body{padding:6px 11px 0}
.card--lg .card-title{font-size:10.5px}
.card--lg .card-text{font-size:8px;margin-top:8px}
.card--lg .card-meta{font-size:8px;margin-bottom:10px;gap:8px}
.card--lg .os i{width:7px;height:7px}
.card--lg .sep{height:9px}
.card--lg .play{font-size:6px;padding:2px 7px}

.cover--eyes{background:linear-gradient(160deg,#1e4a6e,#56b83a 55%,#e7e04a)}
.cover--pitch{background:linear-gradient(170deg,#15305a,#2e6fb8 45%,#3f9a3a)}
.cover--ruins{background:linear-gradient(150deg,#394253,#5f6a78 60%,#2b313a)}
.cover--sky{background:linear-gradient(160deg,#5d8fd8,#9fc2f2 55%,#e8e3d4)}
.cover--planet{background:linear-gradient(120deg,#10183a,#2d3a8a 60%,#c46a3a)}
.cover--red{background:linear-gradient(160deg,#1a1a1a,#b8142a 65%,#2a0c10)}
.cover--metal{background:linear-gradient(160deg,#6a6d70,#8d7060 55%,#3b2c28)}
.cover--fire{background:linear-gradient(160deg,#1b2030,#c8502a 60%,#d8a040)}
.cover--sepia{background:linear-gradient(160deg,#6b4a30,#a07a48 55%,#3a2818)}
.cover--road{background:linear-gradient(160deg,#9bb4c8,#c8a870 55%,#6a5030)}
.cover--night{background:linear-gradient(160deg,#0f1a3a,#2a3a7a 55%,#c42a3a)}
.cover--gold{background:linear-gradient(160deg,#5a3a18,#c8902a 55%,#7a4a1a)}
.cover--forest{background:linear-gradient(160deg,#2a4a2a,#6aa040 55%,#c8b860)}
.cover--ember{background:linear-gradient(160deg,#2a0a0a,#a01818 55%,#3a0808)}
.cover--steel{background:linear-gradient(160deg,#2a3a4a,#6a7c8a 55%,#1a2430)}
.cover--smoke{background:linear-gradient(160deg,#3a3a3a,#7a7a7a 55%,#2a2a2a)}
.cover--candy{background:linear-gradient(160deg,#d82a3a,#f0e0c8 55%,#8a1a1a)}
.cover--bronze{background:linear-gradient(160deg,#5a4a2a,#c8a060 55%,#3a2a18)}
.cover--pastel{background:linear-gradient(160deg,#5ad0f0,#f08ad0 55%,#f0d84a)}
.cover--toxic{background:linear-gradient(160deg,#2a3a10,#8ac02a 55%,#1a2008)}

.news-photo{background:linear-gradient(150deg,#1a1030,#5a1a6a 45%,#c02a5a 75%,#2a1a40)}
.news-photo--b{background:linear-gradient(150deg,#3a1a7a,#a02ad0 45%,#f04ab0 75%,#2a1050)}
.news-photo--c{background:linear-gradient(150deg,#0a0a1a,#2a1a3a 45%,#d0183a 75%,#1a0a1a)}
</style>
</head>
<body>
<div class="canvas">

  <svg class="stage-band" viewBox="0 0 1200 2799" aria-hidden="true">
    <polygon points="0,152 1200,467 1200,734 0,418" fill="#1765ff"/>
  </svg>

  <!-- Desktop hero screen -->
  <section class="abs" style="left:171px;top:128px;width:668px;height:437px;background:var(--page);overflow:hidden">
    <nav class="nav" style="height:38px">
      <span class="brand abs" style="left:72px;font-size:12.5px">PlayerMetricsHubOnline</span>
      <div class="nav-links" style="left:272px;font-size:6.5px"><span>Home</span><span>Vaporo</span><span>Games</span><span>About us</span></div>
      <span class="signin" style="left:502px;font-size:6.5px">Signin</span>
      <span class="btn abs" style="left:533px;width:42px;height:13px;font-size:6px">Login</span>
      <svg class="abs" style="left:584px" width="11" height="11" viewBox="0 0 12 12" aria-hidden="true"><circle cx="5" cy="5" r="3.8" fill="none" stroke="#fff" stroke-width="1.2"/><line x1="8" y1="8" x2="11" y2="11" stroke="#fff" stroke-width="1.2"/></svg>
    </nav>
    <div class="hero-photo" role="img" aria-label="Gaming desk with headphones and keyboard under pink neon light" style="left:0;top:38px;width:668px;height:323px;border-radius:0 0 0 30px"></div>
    <div class="hero-copy" style="left:111px;top:128px">
      <div class="hero-brand" style="font-size:15px">PlayerMetricsHubOnline</div>
      <div class="hero-title" style="font-size:28px;margin-top:6px">Power Up and Play</div>
      <p style="font-size:10.5px;line-height:1.45;margin-top:8px;width:185px">The next challenge is waiting for you. Ready to conquer?</p>
    </div>
    <div class="search-panel" style="left:105px;top:276px;width:456px;height:109px">
      <h3 style="left:28px;top:20px;font-size:12.5px">Search for Platforms/Games</h3>
      <div class="field" style="left:26px;top:48px;width:405px;height:30px;border-radius:3px;font-size:10px">
        <span style="padding-left:13px;width:213px;border-right:1px solid #ddd">Search</span>
        <span style="padding-left:13px;font-size:7px;width:95px;display:flex;justify-content:space-between;align-items:center;padding-right:10px">Platforms<i class="caret"></i></span>
        <span class="btn" style="width:91px;height:23px;font-size:8px;margin-left:2px">
          <svg width="9" height="9" viewBox="0 0 12 12" aria-hidden="true"><circle cx="5" cy="5" r="3.8" fill="none" stroke="#fff" stroke-width="1.3"/><line x1="8" y1="8" x2="11" y2="11" stroke="#fff" stroke-width="1.3"/></svg>Search</span>
      </div>
      <span class="adv" style="right:28px;top:84px;font-size:6.5px">Advance search</span>
    </div>
  </section>

  <!-- Full desktop page -->
  <main class="abs" style="left:103px;top:736px;width:643px;height:1949px;background:var(--page);overflow:hidden">
    <nav class="nav" style="height:39px">
      <span class="brand abs" style="left:71px;font-size:12.5px">PlayerMetricsHubOnline</span>
      <div class="nav-links" style="left:262px"><span>Home</span><span>Vaporo</span><span>Games</span><span>About us</span></div>
      <span class="signin" style="left:482px">Signin</span>
      <span class="btn abs" style="left:513px;width:40px;height:14px;font-size:6px">Login</span>
      <svg class="abs" style="left:563px" width="11" height="11" viewBox="0 0 12 12" aria-hidden="true"><circle cx="5" cy="5" r="3.8" fill="none" stroke="#fff" stroke-width="1.2"/><line x1="8" y1="8" x2="11" y2="11" stroke="#fff" stroke-width="1.2"/></svg>
    </nav>
    <div class="hero-photo" role="img" aria-label="Gaming desk with headphones and keyboard under pink neon light" style="left:0;top:39px;width:643px;height:308px;border-radius:0 0 30px 30px"></div>
    <div class="hero-copy" style="left:108px;top:122px">
      <div class="hero-brand" style="font-size:15px">PlayerMetricsHubOnline</div>
      <div class="hero-title" style="font-size:26px;margin-top:6px">Power Up and Play</div>
      <p style="font-size:10px;line-height:1.45;margin-top:7px;width:180px">The next challenge is waiting for you. Ready to conquer?</p>
    </div>
    <div class="search-panel" style="left:103px;top:265px;width:436px;height:106px">
      <h3 style="left:27px;top:20px;font-size:12.5px">Search for Platforms/Games</h3>
      <div class="field" style="left:25px;top:48px;width:387px;height:28px;border-radius:3px;font-size:9.5px">
        <span style="padding-left:12px;width:205px;border-right:1px solid #ddd">Search</span>
        <span style="padding-left:12px;font-size:6.5px;width:91px;display:flex;justify-content:space-between;align-items:center;padding-right:10px">Platforms<i class="caret"></i></span>
        <span class="btn" style="width:87px;height:22px;font-size:8px;margin-left:2px">
          <svg width="9" height="9" viewBox="0 0 12 12" aria-hidden="true"><circle cx="5" cy="5" r="3.8" fill="none" stroke="#fff" stroke-width="1.3"/><line x1="8" y1="8" x2="11" y2="11" stroke="#fff" stroke-width="1.3"/></svg>Search</span>
      </div>
      <span class="adv" style="right:28px;top:82px;font-size:6.5px">Advance search</span>
    </div>

    <h2 class="abs" style="left:77px;top:430px;font-size:17px;font-weight:500">Search Result</h2>
    <span class="abs" style="left:375px;top:436px;font-size:6.5px">Sort by:</span>
    <div class="field" style="left:415px;top:429px;width:152px;height:21px;font-size:6.5px;color:#333">
      <span style="padding-left:9px;flex:1">Platforms</span>
      <span class="btn" style="width:23px;height:21px;border-radius:0 2px 2px 0"><i class="caret" style="border-top-color:#fff"></i></span>
    </div>

    <article class="card" style="left:64px;top:490px"><div class="cover cover--eyes" role="img" aria-label="Game cover art with staring green eyes"></div><div class="card-body"><div class="card-title">Beyond the Tides</div><p class="card-text">Lörem ipsum taliban-tv rack klimatångest prekiheten.</p><div class="card-meta"><span class="os"><i></i><i></i></span><span class="sep"></span><span>RPG</span><span class="play">PLAY</span></div></div></article>
    <article class="card" style="left:196px;top:490px"><div class="cover cover--pitch" role="img" aria-label="Game cover art of a football match"></div><div class="card-body"><div class="card-title">Beyond the Tides</div><p class="card-text">Lörem ipsum taliban-tv rack klimatångest prekiheten.</p><div class="card-meta"><span class="os"><i></i><i></i></span><span class="sep"></span><span>QLV</span><span class="play">PLAY</span></div></div></article>
    <article class="card" style="left:327px;top:490px"><div class="cover cover--ruins" role="img" aria-label="Game cover art of a dark castle"></div><div class="card-body"><div class="card-title">Beyond the Tides</div><p class="card-text">Lörem ipsum taliban-tv rack klimatångest prekiheten.</p><div class="card-meta"><span class="os"><i></i><i></i></span><span class="sep"></span><span>RPG</span><span class="play">PLAY</span></div></div></article>
    <article class="card" style="left:458px;top:490px"><div class="cover cover--sky" role="img" aria-label="Game cover art with clay lettering on blue sky"></div><div class="card-body"><div class="card-title">Beyond the Tides</div><p class="card-text">Lörem ipsum taliban-tv rack klimatångest prekiheten.</p><div class="card-meta"><span class="os"><i></i><i></i></span><span class="sep"></span><span>QLV</span><span class="play">PLAY</span></div></div></article>

    <article class="card" style="left:64px;top:624px"><div class="cover cover--planet" role="img" aria-label="Game cover art of a planet in space"></div><div class="card-body"><div class="card-title">Beyond the Tides</div><p class="card-text">Lörem ipsum taliban-tv rack klimatångest prekiheten.</p><div class="card-meta"><span class="os"><i></i><i></i></span><span class="sep"></span><span>QLV</span><span class="play">PLAY</span></div></div></article>
    <article class="card" style="left:196px;top:624px"><div class="cover cover--red" role="img" aria-label="Game cover art with red star emblem"></div><div class="card-body"><div class="card-title">Beyond the Tides</div><p class="card-text">Lörem ipsum taliban-tv rack klimatångest prekiheten.</p><div class="card-meta"><span class="os"><i></i><i></i></span><span class="sep"></span><span>RPG</span><span class="play">PLAY</span></div></div></article>
    <article class="card" style="left:327px;top:624px"><div class="cover cover--metal" role="img" aria-label="Game cover art with metal arena emblem"></div><div class="card-body"><div class="card-title">Beyond the Tides</div><p class="card-text">Lörem ipsum taliban-tv rack klimatångest prekiheten.</p><div class="card-meta"><span class="os"><i></i><i></i></span><span class="sep"></span><span>QLV</span><span class="play">PLAY</span></div></div></article>
    <article class="card" style="left:458px;top:624px"><div class="cover cover--fire" role="img" aria-label="Game cover art of a spy action scene"></div><div class="card-body"><div class="card-title">Beyond the Tides</div><p class="card-text">Lörem ipsum taliban-tv rack klimatångest prekiheten.</p><div class="card-meta"><span class="os"><i></i><i></i></span><span class="sep"></span><span>RPG</span><span class="play">PLAY</span></div></div></article>

    <article class="card" style="left:64px;top:758px"><div class="cover cover--sepia" role="img" aria-label="Game cover art of a mystery adventure"></div><div class="card-body"><div class="card-title">Beyond the Tides</div><p class="card-text">Lörem ipsum taliban-tv rack klimatångest prekiheten.</p><div class="card-meta"><span class="os"><i></i><i></i></span><span class="sep"></span><span>RPG</span><span class="play">PLAY</span></div></div></article>
    <article class="card" style="left:196px;top:758px"><div class="cover cover--road" role="img" aria-label="Game cover art of a classic car on a street"></div><div class="card-body"><div class="card-title">Beyond the Tides</div><p class="card-text">Lörem ipsum taliban-tv rack klimatångest prekiheten.</p><div class="card-meta"><span class="os"><i></i><i></i></span><span class="sep"></span><span>QLV</span><span class="play">PLAY</span></div></div></article>
    <article class="card" style="left:327px;top:758px"><div class="cover cover--night" role="img" aria-label="Game cover art of a stick figure fight"></div><div class="card-body"><div class="card-title">Beyond the Tides</div><p class="card-text">Lörem ipsum taliban-tv rack klimatångest prekiheten.</p><div class="card-meta"><span class="os"><i></i><i></i></span><span class="sep"></span><span>RPG</span><span class="play">PLAY</span></div></div></article>
    <article class="card" style="left:458px;top:758px"><div class="cover cover--gold" role="img" aria-label="Game cover art of a steampunk city"></div><div class="card-body"><div class="card-title">Beyond the Tides</div><p class="card-text">Lörem ipsum taliban-tv rack klimatångest prekiheten.</p><div class="card-meta"><span class="os"><i></i><i></i></span><span class="sep"></span><span>QLV</span><span class="play">PLAY</span></div></div></article>

    <article class="card" style="left:64px;top:892px"><div class="cover cover--forest" role="img" aria-label="Game cover art of a fantasy hero in a forest"></div><div class="card-body"><div class="card-title">Beyond the Tides</div><p class="card-text">Lörem ipsum taliban-tv rack klimatångest prekiheten.</p><div class="card-meta"><span class="os"><i></i><i></i></span><span class="sep"></span><span>RPG</span><span class="play">PLAY</span></div></div></article>
    <article class="card" style="left:196px;top:892px"><div class="cover cover--ember" role="img" aria-label="Game cover art with red glow"></div><div class="card-body"><div class="card-title">Beyond the Tides</div><p class="card-text">Lörem ipsum taliban-tv rack klimatångest prekiheten.</p><div class="card-meta"><span class="os"><i></i><i></i></span><span class="sep"></span><span>QLV</span><span class="play">PLAY</span></div></div></article>
    <article class="card" style="left:327px;top:892px"><div class="cover cover--steel" role="img" aria-label="Game cover art with bold title lettering"></div><div class="card-body"><div class="card-title">Beyond the Tides</div><p class="card-text">Lörem ipsum taliban-tv rack klimatångest prekiheten.</p><div class="card-meta"><span class="os"><i></i><i></i></span><span class="sep"></span><span>RPG</span><span class="play">PLAY</span></div></div></article>
    <article class="card" style="left:458px;top:892px"><div class="cover cover--smoke" role="img" aria-label="Game cover art of soldiers in smoke"></div><div class="card-body"><div class="card-title">Beyond the Tides</div><p class="card-text">Lörem ipsum taliban-tv rack klimatångest prekiheten.</p><div class="card-meta"><span class="os"><i></i><i></i></span><span class="sep"></span><span>QLV</span><span class="play">PLAY</span></div></div></article>

    <span class="btn abs" style="left:290px;top:1052px;width:62px;height:15px;font-size:6px;border-radius:4px">Load More</span>

    <section class="abs" style="left:0;top:1122px;width:643px;height:298px;background:var(--blue)">
      <h2 class="abs" style="left:68px;top:69px;font-size:16px;font-weight:500;white-space:nowrap">New Release</h2>
      <p class="abs" style="left:196px;top:71px;width:296px;font-size:6px;line-height:1.45">Lörem ipsum presa kroliga ifall fagån. Ninade telell seledes. Remurer sorade även om ber. Hembränd geost vöpred podat passivhus. Osen monorar, pofaska i beråssade.</p>
      <span class="btn abs" style="left:508px;top:70px;width:59px;height:14px;font-size:6px;background:#111">View More</span>
      <article class="card" style="left:64px;top:110px"><div class="cover cover--candy" role="img" aria-label="Game cover art of toy cars"></div><div class="card-body"><div class="card-title">Beyond the Tides</div><p class="card-text">Lörem ipsum taliban-tv rack klimatångest prekiheten.</p><div class="card-meta"><span class="os"><i></i><i></i></span><span class="sep"></span><span>RPG</span><span class="play">PLAY</span></div></div></article>
      <article class="card" style="left:196px;top:110px"><div class="cover cover--bronze" role="img" aria-label="Game cover art with round emblem"></div><div class="card-body"><div class="card-title">Beyond the Tides</div><p class="card-text">Lörem ipsum taliban-tv rack klimatångest prekiheten.</p><div class="card-meta"><span class="os"><i></i><i></i></span><span class="sep"></span><span>QLV</span><span class="play">PLAY</span></div></div></article>
      <article class="card" style="left:327px;top:110px"><div class="cover cover--pastel" role="img" aria-label="Game cover art of colourful party characters"></div><div class="card-body"><div class="card-title">Beyond the Tides</div><p class="card-text">Lörem ipsum taliban-tv rack klimatångest prekiheten.</p><div class="card-meta"><span class="os"><i></i><i></i></span><span class="sep"></span><span>RPG</span><span class="play">PLAY</span></div></div></article>
      <article class="card" style="left:458px;top:110px"><div class="cover cover--toxic" role="img" aria-label="Game cover art with green sci-fi glow"></div><div class="card-body"><div class="card-title">Beyond the Tides</div><p class="card-text">Lörem ipsum taliban-tv rack klimatångest prekiheten.</p><div class="card-meta"><span class="os"><i></i><i></i></span><span class="sep"></span><span>QLV</span><span class="play">PLAY</span></div></div></article>
    </section>

    <h2 class="abs" style="left:0;width:643px;text-align:center;top:1468px;font-size:16px;font-weight:500">Latest News</h2>
    <p class="abs" style="left:125px;width:393px;text-align:center;top:1497px;font-size:6px;line-height:1.5">Lörem ipsum presa kroliga ifall fagån. Ninade telell seledes. Remurer sorade även om ber. Hembränd geost vöpred podat passivhus. Osen monorar, pofaska i beråssade.</p>

    <article class="abs" style="left:78px;top:1536px;width:152px">
      <div class="news-photo" role="img" aria-label="Streamer playing at a neon lit gaming setup" style="height:103px"></div>
      <p style="font-size:5.5px;margin-top:13px;color:var(--muted)">Dec 16, 2024 &nbsp;|&nbsp; No Comments</p>
      <h4 style="font-size:7.5px;font-weight:600;line-height:1.3;margin-top:6px">Velit dapibus sollicitudin sit iaculis ipsum dolor sit amet</h4>
      <span class="btn" style="width:59px;height:14px;font-size:6px;margin-top:6px">Read More</span>
    </article>
    <article class="abs" style="left:245px;top:1536px;width:152px">
      <div class="news-photo news-photo--b" role="img" aria-label="Two players gaming in a purple lit room" style="height:103px"></div>
      <p style="font-size:5.5px;margin-top:13px;color:var(--muted)">Dec 16, 2024 &nbsp;|&nbsp; No Comments</p>
      <h4 style="font-size:7.5px;font-weight:600;line-height:1.3;margin-top:6px">Velit dapibus sollicitudin sit iaculis ipsum dolor sit amet</h4>
      <span class="btn" style="width:59px;height:14px;font-size:6px;margin-top:6px">Read More</span>
    </article>
    <article class="abs" style="left:411px;top:1536px;width:152px">
      <div class="news-photo news-photo--c" role="img" aria-label="Player at a desk with red glowing monitors" style="height:103px"></div>
      <p style="font-size:5.5px;margin-top:13px;color:var(--muted)">Dec 16, 2024 &nbsp;|&nbsp; No Comments</p>
      <h4 style="font-size:7.5px;font-weight:600;line-height:1.3;margin-top:6px">Velit dapibus sollicitudin sit iaculis ipsum dolor sit amet</h4>
      <span class="btn" style="width:59px;height:14px;font-size:6px;margin-top:6px">Read More</span>
    </article>

    <footer class="abs" style="left:0;top:1764px;width:643px;height:185px;background:var(--footer)">
      <span class="brand abs" style="left:82px;top:55px;font-size:12px">PlayerMetricsHubOnline</span>
      <p class="abs" style="left:82px;top:80px;width:135px;font-size:5.5px;line-height:1.45">Lörem ipsum decinade reaskapet sörade det trafoning i sadade. Prektigt. Trasm trirad. Sofesam kavedir. Seskapet safojäd då treskade.</p>
      <h4 class="abs" style="left:262px;top:44px;font-size:12px;font-weight:500">Company</h4>
      <ul class="abs" style="left:262px;top:70px;list-style:none;font-size:5.5px;line-height:2.25">
        <li>Home</li><li>Vaporo</li><li>Games</li><li>About us</li><li>Contact us</li>
      </ul>
      <h4 class="abs" style="left:371px;top:44px;font-size:12px;font-weight:500;white-space:nowrap">Sign up to our newsletter</h4>
      <p class="abs" style="left:371px;top:67px;font-size:5.5px;white-space:nowrap">Submit email and signup for monthly newsletters</p>
      <div class="field" style="left:369px;top:82px;width:182px;height:21px;border-radius:3px;font-size:6.5px;color:#333">
        <span style="padding-left:10px;flex:1">Email here...</span>
        <span class="btn" style="width:67px;height:21px;font-size:6.5px;border-radius:0 3px 3px 0">Sign up</span>
      </div>
      <div class="abs" style="left:371px;top:117px;display:flex;gap:7px" aria-label="Social links">
        <i style="display:block;width:10px;height:10px;border-radius:50%;background:#fff"></i>
        <i style="display:block;width:10px;height:10px;border-radius:50%;background:#fff"></i>
        <i style="display:block;width:10px;height:10px;border-radius:50%;background:#fff"></i>
        <i style="display:block;width:10px;height:10px;border-radius:50%;background:#fff"></i>
      </div>
      <div class="abs" style="left:49px;top:159px;width:545px;height:1px;background:var(--line)"></div>
      <p class="abs" style="left:0;width:643px;text-align:center;top:169px;font-size:5.5px">Copyright ©2024 PlayerMetricsHubOnline. All Rights Reserved.</p>
    </footer>
  </main>

  <!-- Mobile page -->
  <section class="abs" style="left:814px;top:201px;width:232px;height:1397px;background:var(--page);overflow:hidden">
    <nav class="nav" style="height:33px">
      <span class="brand abs" style="left:12px;font-size:10px">PlayerMetricsHubOnline</span>
      <svg class="abs" style="left:208px" width="11" height="9" viewBox="0 0 11 9" aria-hidden="true"><rect width="11" height="1.2" fill="#fff"/><rect y="3.9" width="11" height="1.2" fill="#fff"/><rect y="7.8" width="11" height="1.2" fill="#fff"/></svg>
    </nav>
    <div class="hero-photo" role="img" aria-label="Gaming desk with headphones and keyboard under pink neon light" style="left:0;top:33px;width:232px;height:480px"></div>
    <div class="hero-copy" style="left:17px;top:148px;width:200px">
      <div class="hero-brand" style="font-size:18px;line-height:1.25">PlayerMetricsHub<br>Online</div>
      <div class="hero-title" style="font-size:33px;margin-top:10px">Power Up and Play</div>
      <p style="font-size:13px;line-height:1.45;margin-top:12px">The next challenge is waiting for you. Ready to conquer?</p>
    </div>
    <div class="search-panel" style="left:10px;top:421px;width:212px;height:255px">
      <h3 style="left:20px;top:30px;font-size:16px;line-height:1.3">Search for Platforms/Games</h3>
      <div class="field" style="left:15px;top:82px;width:186px;height:36px;border-radius:3px;font-size:12px;padding-left:16px">Search</div>
      <div class="field" style="left:15px;top:126px;width:186px;height:36px;border-radius:3px;font-size:9px;padding:0 14px 0 16px;justify-content:space-between">Platforms<i class="caret"></i></div>
      <span class="btn abs" style="left:15px;top:170px;width:186px;height:37px;font-size:11px">
        <svg width="12" height="12" viewBox="0 0 12 12" aria-hidden="true"><circle cx="5" cy="5" r="3.8" fill="none" stroke="#fff" stroke-width="1.2"/><line x1="8" y1="8" x2="11" y2="11" stroke="#fff" stroke-width="1.2"/></svg>Search</span>
      <span class="adv" style="right:17px;top:222px;font-size:8px">Advance search</span>
    </div>

    <h2 class="abs" style="left:0;width:232px;text-align:center;top:718px;font-size:22px;font-weight:500">Search Result</h2>
    <span class="abs" style="left:28px;top:767px;font-size:9px">Sort by:</span>
    <div class="field" style="left:16px;top:785px;width:200px;height:25px;border-radius:2px;font-size:8px;color:#333">
      <span style="padding-left:12px;flex:1">Platforms</span>
      <span class="btn" style="width:29px;height:25px;border-radius:0 2px 2px 0"><i class="caret" style="border-top-color:#fff"></i></span>
    </div>

    <article class="card card--lg" style="left:17px;top:853px"><div class="cover cover--eyes" role="img" aria-label="Game cover art with staring green eyes"></div><div class="card-body"><div class="card-title">Beyond the Tides</div><p class="card-text">Lörem ipsum taliban-tv rack klimatångest prekiheten.</p><div class="card-meta"><span class="os"><i></i><i></i></span><span class="sep"></span><span>RPG</span><span class="play">PLAY</span></div></div></article>
    <article class="card card--lg" style="left:17px;top:1023px"><div class="cover cover--pitch" role="img" aria-label="Game cover art of a football match"></div><div class="card-body"><div class="card-title">Beyond the Tides</div><p class="card-text">Lörem ipsum taliban-tv rack klimatångest prekiheten.</p><div class="card-meta"><span class="os"><i></i><i></i></span><span class="sep"></span><span>QLV</span><span class="play">PLAY</span></div></div></article>
    <article class="card card--lg" style="left:17px;top:1192px"><div class="cover cover--ruins" role="img" aria-label="Game cover art of a dark castle"></div><div class="card-body"><div class="card-title">Beyond the Tides</div><p class="card-text">Lörem ipsum taliban-tv rack klimatångest prekiheten.</p><div class="card-meta"><span class="os"><i></i><i></i></span><span class="sep"></span><span>RPG</span><span class="play">PLAY</span></div></div></article>
  </section>

</div>
</body>
</html>
```